Tov Fiesta Mariners

We are party planning business. We are a team of established individuals and business in party stream businesses like DJ, Caterers, Party supplies, Kids parties, Events & Private Parties and much more. So basically me and business collaborate a team of business or individuals to do clients party in the best way possible.

Target Market(s)

majority of them 16 to 30 -60% to 70 % and 30 to 40 year olds- 30% to 40 %

Industry/Entity Type

Party Planning

Contact Information for Business Card

Tov
Owner & Manager
0471829354
tovfiestamariners@mailpost.example

Requirements
Must have
• front side : Logo and list of services we provide
DJ's, Catering,All party supplies, Tinyjubilee and more...just to show what the business is about when anyone looks at the card and at the rear side my details which are already provided.
Should not have
• Dont make it look we do kids party which is just one of the things we do but don't make my business card look like kids party specialist make it more connecting to youngsters and older crowd more

```html
<!DOCTYPE html>
<html lang="en">
<head>
<meta charset="utf-8">
<title>Tov Fiesta Mariners — Business Cards</title>
<link rel="stylesheet" href="https://fonts.googleapis.com/css2?family=Kaushan+Script&display=swap">
<style>
  :root {
    --backdrop: #e4e2df;
    --card-light: #dcdcdc;
    --card-mid: #c9c9c9;
    --card-edge: #b4b4b4;
    --accent-red: #d8232a;
    --ink: #1f1f1f;
    --script: "Kaushan Script", cursive;
  }
  * { box-sizing: border-box; margin: 0; padding: 0; }
  html, body {
    width: 1200px;
    height: 873px;
    overflow: hidden;
    background: var(--backdrop);
  }
  .stage {
    position: relative;
    width: 1200px;
    height: 873px;
    display: flex;
    align-items: center;
    justify-content: center;
    gap: 60px;
  }
  .card {
    position: relative;
    width: 525px;
    height: 300px;
    border-radius: 3px;
    background: radial-gradient(ellipse at 45% 40%, var(--card-light), var(--card-mid) 75%);
    box-shadow: 0 1px 0 var(--card-edge), 0 12px 28px rgba(0, 0, 0, 0.18);
    font-family: var(--script);
  }
  .brand {
    position: absolute;
    display: flex;
    align-items: center;
    gap: 12px;
  }
  .brand-dot {
    width: 18px;
    height: 18px;
    border-radius: 50%;
    background: var(--accent-red);
    flex: none;
  }
  .brand-name {
    color: var(--accent-red);
    font-size: 30px;
    line-height: 1.05;
    width: 170px;
  }

  /* details side */
  .card--details .brand { left: 40px; top: 100px; }
  .details {
    position: absolute;
    left: 290px;
    top: 60px;
    display: flex;
    flex-direction: column;
  }
  .details-name {
    color: var(--accent-red);
    font-size: 40px;
    line-height: 1;
  }
  .details-role {
    color: var(--ink);
    font-size: 15px;
    margin-top: 10px;
  }
  .details-phone {
    color: var(--accent-red);
    font-size: 17px;
    margin-top: 48px;
  }
  .details-email {
    color: var(--accent-red);
    font-size: 14px;
    margin-top: 14px;
    white-space: nowrap;
  }

  /* services side */
  .card--services .brand {
    left: 50%;
    top: 70px;
    transform: translateX(-50%);
  }
  .card--services .brand-name { text-align: left; }
  .services {
    position: absolute;
    left: 0;
    right: 0;
    bottom: 42px;
    text-align: center;
    color: var(--accent-red);
    font-size: 17px;
  }
</style>
</head>
<body>
  <main class="stage">
    <section class="card card--details" aria-label="Contact side">
      <div class="brand">
        <span class="brand-dot"></span>
        <span class="brand-name">Tov Fiesta Mariners</span>
      </div>
      <div class="details">
        <p class="details-name">Tov</p>
        <p class="details-role">Owner &amp; Manager</p>
        <p class="details-phone">0471829354</p>
        <p class="details-email">tovfiestamariners@mailpost.example</p>
      </div>
    </section>

    <section class="card card--services" aria-label="Services side">
      <div class="brand">
        <span class="brand-dot"></span>
        <span class="brand-name">Tov Fiesta Mariners</span>
      </div>
      <p class="services">DJ's, catering, all party supplies, Tinyjubilee and more...</p>
    </section>
  </main>
</body>
</html>
```